Design a powerpoint background using company logo/colours

We require a powerpoint background that incorporates our company colours and logo. I have attached the logo in various sizes.

Have fun and be imaginative

Our company colours are white and Red-236, Green-22 and Blue 86.
Please use these colours in designing the ppt background

Industry/Entity Type

It Company

Colors

Designer to choose colors to be used in the design.

```html
<!DOCTYPE html>
<html lang="en">
<head>
<meta charset="utf-8">
<title>Project Title Here</title>
<link rel="stylesheet" href="https://fonts.googleapis.com/css2?family=Exo+2:wght@700&family=PT+Sans:wght@700&family=Archivo+Narrow:wght@400&display=swap">
<style>
  :root {
    --brand-red: #ec1656;
    --white: #ffffff;
    --ink: #222222;
    --header-grey: #f3f3f3;
    --tagline-grey: #8a8a8a;
  }
  * { margin: 0; padding: 0; box-sizing: border-box; }
  html, body {
    width: 1200px;
    height: 900px;
    overflow: hidden;
    background: var(--white);
  }
  .slide {
    position: relative;
    width: 1200px;
    height: 900px;
    background: var(--white);
    overflow: hidden;
  }
  .title-band {
    position: absolute;
    left: 0; top: 0;
    width: 930px; height: 96px;
    background: var(--brand-red);
  }
  .slide-title {
    position: absolute;
    left: 28px; top: 18px;
    font-family: "Exo 2", sans-serif;
    font-weight: 700;
    font-size: 46px;
    line-height: 56px;
    color: var(--white);
    letter-spacing: 0.5px;
  }
  .brand-panel {
    position: absolute;
    left: 930px; top: 0;
    width: 270px; height: 96px;
    background: var(--header-grey);
    display: flex;
    flex-direction: column;
    justify-content: center;
    align-items: center;
  }
  .brand-name {
    display: flex;
    align-items: center;
    gap: 10px;
    font-family: "PT Sans", sans-serif;
    font-weight: 700;
    font-size: 40px;
    line-height: 44px;
    color: var(--brand-red);
  }
  .brand-square {
    width: 26px; height: 26px;
    background: var(--brand-red);
  }
  .brand-tagline {
    margin-top: 4px;
    font-family: "Archivo Narrow", sans-serif;
    font-size: 12px;
    color: var(--tagline-grey);
  }
  .content-column {
    position: absolute;
    top: 180px;
    width: 485px;
  }
  .content-column.left { left: 60px; }
  .content-column.right { left: 648px; }
  .column-heading {
    font-family: "PT Sans", sans-serif;
    font-weight: 700;
    font-size: 31px;
    line-height: 40px;
    color: var(--brand-red);
    margin-bottom: 6px;
  }
  .column-body {
    font-family: "Archivo Narrow", sans-serif;
    font-size: 21px;
    line-height: 30px;
    color: var(--ink);
    text-align: justify;
    margin-bottom: 30px;
  }
  .column-body.trailing { text-align-last: justify; }
  .footer-band {
    position: absolute;
    left: 0; bottom: 0;
    width: 1200px; height: 48px;
    background: var(--brand-red);
  }
</style>
</head>
<body>
<main class="slide">
  <header class="title-band">
    <h1 class="slide-title">Project Title Here</h1>
  </header>
  <div class="brand-panel">
    <div class="brand-name"><span>Nodexa</span><span class="brand-square"></span></div>
    <div class="brand-tagline">Connected ideas, delivered</div>
  </div>

  <section class="content-column left">
    <h2 class="column-heading">Subtext here</h2>
    <p class="column-body">Lorem ipsum dolor sit Lorem ipsum dolor sit&nbsp; Lorem ipsum dolor sit Lorem ipsum dolor sit&nbsp; Lorem ipsum dolor sit Lorem ipsum dolor sit Lorem ipsum dolor sit.</p>
    <p class="column-body">Lorem ipsum dolor sit&nbsp; Lorem ipsum dolor sit Lorem ipsum dolor sit&nbsp; Lorem ipsum Lorem ipsum dolor sit Lorem ipsum dolor sit&nbsp; Lorem ipsum dolor sit Lorem ipsum dolor sit&nbsp; Lorem ipsum dolor sit Lorem ipsum dolor sit Lorem ipsum dolor sit.</p>
    <p class="column-body trailing">Lorem ipsum dolor sit&nbsp; Lorem ipsum dolor sit Lorem</p>
  </section>

  <section class="content-column right">
    <h2 class="column-heading">Subtext here</h2>
    <p class="column-body">Lorem ipsum dolor sit Lorem ipsum dolor sit&nbsp; Lorem ipsum dolor sit Lorem ipsum dolor sit&nbsp; Lorem ipsum dolor sit Lorem ipsum dolor sit Lorem ipsum dolor sit.</p>
    <p class="column-body">Lorem ipsum dolor sit&nbsp; Lorem ipsum dolor sit Lorem ipsum dolor sit&nbsp; Lorem ipsum Lorem ipsum dolor sit Lorem ipsum dolor sit&nbsp; Lorem ipsum dolor sit Lorem ipsum dolor sit&nbsp; Lorem ipsum dolor sit Lorem ipsum dolor sit Lorem ipsum dolor sit.</p>
    <p class="column-body trailing">Lorem ipsum dolor sit&nbsp; Lorem ipsum dolor sit Lorem</p>
  </section>

  <footer class="footer-band"></footer>
</main>
</body>
</html>
```